The Varrow Ledger: Book Cover

I need a book cover for the English language version of a counterfactual history thriller, a story that takes off where "Greyhollow" by Edwin Calloway ends.

1983: Germany has won the war, the postwar time has brought prosperity and peace to Europe. The Wild East is no longer wild, only beyond the Urals do scattered Soviet units still occasionally carry out attacks against the Wehrmacht administration and German settlers.
Konrad Bielke, born in Stuttgart and a criminalist with heart and soul, is district chief in Hartmannstadt a.d. Medritz, and thus simultaneously the highest police officer, judge, representative of the Reich and the SS. Ten years earlier, he had been transferred to the eastern border of the Reich in order to avoid the unpleasant consequences of his investigations into the machinations of some high-ranking Nazi party members in southern Germany. Bielke likes working in the east, but even here he can't keep his investigator's instincts in check. When a mysterious stranger turns up, Bielke's investigation brings strange things to light. The Gestapo provide the necessary information, but at the same time prevent further investigations by the SS. Despite a warning from his superiors, Bielke cannot let the file rest. When he comes across a well-kept secret about the 1940 peace treaty between Germany, England and France, events take a turn for the worse.
Bielke finds himself on the wrong side of a manhunt which he can only survive with the help of an unlikely ally.

The novel has appeared in German a couple of years ago. I need a book cover for an English language softcover book and an eBook addressed at English speakers. Please, even though the Wehrmacht and Nazi party are mentioned: no swastikas and no openly National Socialist symbols.

Target Market(s)

all English speakers accross the world

Requirements
Should not have
• Swastikas and other offensive signs of the Nazi reign

```html
<!DOCTYPE html>
<html lang="en">
<head>
<meta charset="utf-8">
<title>The Varrow Ledger – Book Cover</title>
<link rel="stylesheet" href="https://fonts.googleapis.com/css2?family=Oswald:wght@500;600&family=Bebas+Neue&display=swap">
<style>
  :root {
    --page-bg: #120606;
    --cover-red: #e8302c;
    --cover-deep: #6a0d0c;
    --cover-black: #0c0707;
    --title-red: #d8221f;
    --ink-dark: #120808;
    --frame-dark: #1c0b0a;
  }
  html, body {
    margin: 0;
    width: 1200px;
    height: 878px;
    overflow: hidden;
    background: var(--page-bg);
  }
  .book-cover {
    position: absolute;
    left: 365px;
    top: 63px;
    width: 470px;
    height: 751px;
    overflow: hidden;
    background: var(--cover-black);
    box-shadow: 0 10px 40px rgba(0,0,0,0.7);
  }
  .cover-art {
    position: absolute;
    inset: 0;
    background:
      radial-gradient(ellipse 60% 40% at 40% 30%, var(--cover-red) 0%, rgba(200,30,28,0.7) 45%, transparent 80%),
      radial-gradient(ellipse 70% 55% at 55% 45%, var(--cover-deep) 0%, transparent 80%),
      linear-gradient(180deg, #a81a18 0%, #3a0908 55%, var(--cover-black) 100%);
  }
  .cover-art::after {
    content: "";
    position: absolute;
    left: 50%;
    top: 90px;
    width: 270px;
    height: 661px;
    transform: translateX(-50%);
    background: linear-gradient(180deg, rgba(10,5,5,0.75), rgba(10,5,5,0.95));
    border-radius: 90px 90px 0 0;
  }
  .author {
    position: absolute;
    top: 30px;
    left: 0;
    right: 0;
    text-align: center;
    font-family: "Oswald", sans-serif;
    font-weight: 500;
    font-size: 30px;
    letter-spacing: 0.5px;
    color: var(--ink-dark);
    margin: 0;
  }
  .title-frame {
    position: absolute;
    left: 27px;
    top: 312px;
    width: 416px;
    height: 236px;
  }
  .title {
    position: absolute;
    left: 0;
    right: 0;
    top: 336px;
    margin: 0;
    text-align: center;
    font-family: "Bebas Neue", sans-serif;
    font-weight: 400;
    color: var(--title-red);
    line-height: 1;
  }
  .title-lead {
    display: block;
    font-family: "Oswald", sans-serif;
    font-weight: 600;
    font-size: 26px;
    letter-spacing: 1px;
  }
  .title-line {
    display: block;
    font-size: 94px;
    letter-spacing: 2px;
    line-height: 0.86;
  }
  .genre {
    position: absolute;
    top: 646px;
    left: 0;
    right: 0;
    text-align: center;
    font-family: "Oswald", sans-serif;
    font-weight: 500;
    font-size: 27px;
    color: var(--title-red);
    margin: 0;
  }
</style>
</head>
<body>
  <main class="book-cover">
    <div class="cover-art" role="img" aria-label="Silhouette of a uniformed officer in a peaked cap standing in red smoke"></div>
    <p class="author">Anselm Draeger</p>
    <svg class="title-frame" viewBox="0 0 416 236" aria-hidden="true">
      <g fill="none" stroke="var(--frame-dark)" stroke-width="5" stroke-opacity="0.85">
        <polyline points="2,22 2,2 412,2 412,22"/>
        <polyline points="2,214 2,234 60,234"/>
        <polyline points="356,234 412,234 412,214"/>
        <line x1="2" y1="40" x2="2" y2="196" stroke-opacity="0.4"/>
      </g>
    </svg>
    <h1 class="title">
      <span class="title-lead">THE</span>
      <span class="title-line">VARROW</span>
      <span class="title-line">LEDGER</span>
    </h1>
    <p class="genre">Thriller</p>
  </main>
</body>
</html>
```